HomeBridle business card and stationary design

We are looking for a simple yet elegant design for our mortgage company business card and stationary.

The card should include:
Name (Derek Walsh)
Title (CEO)
Phone Number (614-208-3917)
Address (48 Birchfield Court, Suite 314, Marlow, OH 43952)
Email (email@homebridle-example.com)
"NMLS" i.e. (NMLS 61947)
"Company NMLS" (Company NMLS 472815)

See above

```html
<!DOCTYPE html>
<html lang="en">
<head>
<meta charset="utf-8">
<title>HomeBridle Business Card</title>
<link rel="stylesheet" href="https://fonts.googleapis.com/css2?family=Montserrat:wght@400;500;600;700&display=swap">
<style>
  :root {
    --backdrop: #8a8a8a;
    --navy: #1a2632;
    --white: #ffffff;
    --sky: #29abe2;
    --ink-light: #f2f4f6;
  }
  * { margin: 0; padding: 0; box-sizing: border-box; }
  html, body {
    width: 1160px;
    height: 1200px;
    overflow: hidden;
  }
  body {
    background: var(--backdrop);
    font-family: "Montserrat", Arial, sans-serif;
    position: relative;
  }
  .card {
    position: absolute;
    left: 199px;
    width: 777px;
    height: 441px;
    border-radius: 30px;
    overflow: hidden;
    background: var(--navy);
  }
  .card-front { top: 105px; }
  .card-back { top: 634px; }

  .brand-panel {
    position: absolute;
    left: 0; top: 0;
    width: 248px;
    height: 100%;
    background: var(--white);
  }
  .brand-vertical {
    position: absolute;
    left: 116px;
    top: 220px;
    transform: translate(-50%, -50%) rotate(-90deg);
    font-size: 50px;
    font-weight: 600;
    color: var(--sky);
    white-space: nowrap;
    letter-spacing: -0.5px;
  }

  .details {
    position: absolute;
    left: 388px;
    top: 0;
    color: var(--ink-light);
  }
  .line {
    position: absolute;
    left: 0;
    height: 26px;
    line-height: 26px;
    white-space: nowrap;
    font-size: 19px;
    font-weight: 400;
  }
  .person-name {
    top: 70px;
    font-size: 25px;
    font-weight: 700;
    color: var(--sky);
    letter-spacing: -0.3px;
  }
  .person-title { top: 100px; font-size: 18px; font-weight: 700; color: var(--white); }
  .nmls { top: 148px; }
  .company-nmls { top: 179px; }
  .contact { left: 0; display: flex; align-items: center; gap: 14px; }
  .contact svg { width: 20px; height: 20px; flex: none; }
  .phone { top: 226px; }
  .email { top: 256px; }
  .website { top: 287px; }
  .address-1 { top: 338px; left: 3px; }
  .address-2 { top: 366px; left: 3px; }

  .brand-centered {
    position: absolute;
    left: 413px;
    top: 254px;
    transform: translate(-50%, -50%);
    font-size: 74px;
    font-weight: 600;
    color: var(--white);
    white-space: nowrap;
    letter-spacing: -1px;
  }
</style>
</head>
<body>
  <section class="card card-front">
    <div class="brand-panel">
      <div class="brand-vertical">HomeBridle</div>
    </div>
    <div class="details">
      <div class="line person-name">DEREK WALSH</div>
      <div class="line person-title">CEO</div>
      <div class="line nmls">"NMLS" i.e. (NMLS 61947)</div>
      <div class="line company-nmls">Company NMLS 472815</div>
      <div class="line contact phone">
        <svg viewBox="0 0 24 24" aria-hidden="true"><path fill="var(--sky)" d="M6.6 10.8a15.2 15.2 0 0 0 6.6 6.6l2.2-2.2a1 1 0 0 1 1-.25 11.4 11.4 0 0 0 3.6.57 1 1 0 0 1 1 1V20a1 1 0 0 1-1 1A17 17 0 0 1 3 4a1 1 0 0 1 1-1h3.5a1 1 0 0 1 1 1c0 1.25.2 2.45.57 3.57a1 1 0 0 1-.25 1z"/><path fill="none" stroke="var(--sky)" stroke-width="1.6" d="M14 3a7 7 0 0 1 7 7M14 6.5a3.5 3.5 0 0 1 3.5 3.5"/></svg>
        <span>614-208-3917</span>
      </div>
      <div class="line contact email">
        <svg viewBox="0 0 24 24" aria-hidden="true"><rect x="2" y="5" width="20" height="14" fill="var(--sky)"/><path d="M2 5l10 8 10-8M2 19l7-7M22 19l-7-7" fill="none" stroke="var(--navy)" stroke-width="1.5"/></svg>
        <span>email@homebridle-example.com</span>
      </div>
      <div class="line contact website">
        <svg viewBox="0 0 24 24" aria-hidden="true"><circle cx="12" cy="12" r="10" fill="var(--sky)"/><path d="M12 2v20M2 12h20M5 6c4 2 10 2 14 0M5 18c4-2 10-2 14 0" fill="none" stroke="var(--navy)" stroke-width="1.2"/></svg>
        <span>www.homebridle.com</span>
      </div>
      <div class="line address-1">48 Birchfield Court, Suite</div>
      <div class="line address-2">314, Marlow, OH 43952)</div>
    </div>
  </section>

  <section class="card card-back">
    <div class="brand-centered">HomeBridle</div>
  </section>
</body>
</html>
```